New logo and packaging for Chicago based skincare company

Venmira needs a new logo and packaging to help in marketing our new anti-aging skincare line.

About Us
We're quirky, skin-obsessed beauty geeks with a knack for research and a love for all things skincare. Our ambition to create REAL products with exotic ingredients inspired the name Venmira which translates to peau + jolie meaning beautiful skin in french.

Our Products
We strive to do it differently. We develop high potency, natural skincare products using top of the line, novel ingredients imported from all over the globe. Our products are made in the USA and free from gluten, parabens, sulfates, and useless fillers that can't deliver.
Price range: $25-75 (moderate)

LOGO
Open to any color/typography except red and purple. Should also be: modern, feminine, cultured, neutral, vibrant, simple, timeless, and sophisticated

LABEL
Logo placed on label, but should not be the focal point of product. EGF SERUM should grab attention of quick glancers
The ideal label design pairs neutrals with brights while achieving balance between minimalism and complexity.
Incorporates some sort of unconventionality, boldness, or uniqueness without adding distraction.

Color: Mostly white or silver background with splash of color (no purple, light pinks, or red). See attached kraft color chart for direction. Bright blues (teal, cobalt, navy, sky blue, and greens are ideal)

Target Market(s)

Target audience: Socially and health conscious women, cultured, ages 25-60, seeks high quality natural products with effective ingredients.

Industry/Entity Type

Skin Care Product

Logo Text

Venmira

Font styles to use
Other font styles liked:
• Open

Colors
f6f6f6
ffffff
fdfdfd
eeeeee
fbfbfb
0255a3
3176b5
33a6d7
86cfc6

Requirements
Must have
• Packaging includes:
• 1 oz amber glass bottles with white dropper - see attached image
• Dimensions: 1.25" width by 4.1" height
• Label should wrap around bottle similar to peptide complex image and includes ingredient list; Logo should be not focal point of label
• Green (peptide complex) label shows ideal clarity
• "NuGlint" can be written in several different ways, feel free to get creative
• Label Text:
• EGF
• NUGLINT
• SERUM
• Anti-aging Skin firming Scar removal
• 1 FL OZ (30ml)
• Ingredients:
• Hamamelis Virginiana (Witch Hazel) Water, Aqua (Water), Alcohol, Glycerin, Polysorbate 20, rh-Oligopeptide-1(EGF), Caprooyl Tetrapeptide-3, Cocos Nucifera (Coconut) Fruit Juice, Lavandula Angustifolia (Lavender) Oil, Citrus
• Paradisi (Pink Grapefruit) Peel Oil*, Citrus Aurantium Dulcis (Orange) Peel Oil*, Santalum Austrocaledonicum (Sandalwood) Wood Oil, Boswellia Carterii (Frankincense) Oil, Rosa Damascena Flower Oil, Dextran, Xanthan Gum,
• Gluconolactone, Sodium Benzoate
• Directions:
• Apply a small amount of EGF serum to clean skin once or twice daily. Allow to dry. Can be used both morning and night, and under makeup. Follow with moisturizer.
• Caution: For external use only. Use only as directed. Avoid contact with eyes. If contact occurs, rinse well with water.
• Distributed by Venmira, LLC
• Munster, Indiana 46398
• Made in USA, FDA Registered lab (please use symbols for these)
Nice to have
• Either or: White space, silver, boldness, numbers, kraft colors (see attached) shapes, geometric patterns, minimalism
• Label: Incorporate shapes and dimensions with minimal/bare background
• Open to handwritten fonts if clear and easy to read
Should not have
• No more than 3-4 colors, look too busy, cursive fonts

```html
<!DOCTYPE html>
<html lang="en">
<head>
<meta charset="utf-8">
<title>Venmira EGF NuGlint Serum Label</title>
<link rel="stylesheet" href="https://fonts.googleapis.com/css2?family=Josefin+Sans:wght@300;400&family=Marcellus&display=swap">
<style>
  :root {
    --backdrop: #e9e2e3;
    --label: #e7e7e7;
    --ink: #3a3a3a;
    --accent-mark: #8a8a8a;
  }
  html, body {
    margin: 0;
    padding: 0;
    width: 1024px;
    height: 1200px;
    overflow: hidden;
    background: var(--backdrop);
  }
  .canvas {
    position: relative;
    width: 1024px;
    height: 1200px;
  }
  .label {
    position: absolute;
    left: 201px;
    top: 123px;
    width: 621px;
    height: 954px;
    background: linear-gradient(90deg, #dedede 0%, var(--label) 18%, #ececec 55%, var(--label) 85%, #dcdcdc 100%);
  }
  .label > * {
    position: absolute;
    left: 0;
    right: 0;
    margin: 0;
    text-align: center;
    line-height: 1;
    color: var(--ink);
    white-space: nowrap;
  }
  .brand-dot {
    left: 280px;
    right: auto;
    top: 66px;
    width: 61px;
    height: 61px;
    border-radius: 50%;
    background: var(--ink);
  }
  .brand-name {
    top: 150px;
    font-family: "Josefin Sans", sans-serif;
    font-weight: 400;
    font-size: 38px;
  }
  .product-code {
    top: 262px;
    font-family: "Josefin Sans", sans-serif;
    font-weight: 300;
    font-size: 230px;
    letter-spacing: 6px;
  }
  .product-name {
    top: 500px;
    font-family: "Josefin Sans", sans-serif;
    font-weight: 300;
    font-size: 80px;
    letter-spacing: -1px;
  }
  .divider-star {
    font-family: "Marcellus", serif;
    font-size: 72px;
    color: var(--accent-mark);
  }
  .divider-star.first { top: 606px; }
  .divider-star.second { top: 775px; }
  .claim { font-family: "Marcellus", serif; }
  .claim.anti-aging { top: 662px; font-size: 42px; }
  .claim.firming { top: 714px; font-size: 36px; }
  .claim.scar { top: 832px; font-size: 34px; }
  .volume {
    top: 874px;
    font-family: "Marcellus", serif;
    font-size: 28px;
  }
</style>
</head>
<body>
<div class="canvas">
  <section class="label">
    <div class="brand-dot"></div>
    <p class="brand-name">Venmira</p>
    <p class="product-code">EGF</p>
    <p class="product-name">NUGLINT</p>
    <p class="divider-star first">*</p>
    <p class="claim anti-aging">Anti aging</p>
    <p class="claim firming">Skin firming</p>
    <p class="divider-star second">*</p>
    <p class="claim scar">Scar removal</p>
    <p class="volume">1 FL OZ (30ml)</p>
  </section>
</div>
</body>
</html>
```